Valmoric Pocket Folder

Create a new pocket folder
An Overview / Background of the Business & Services
We would like a new folder to use when making formal presentations
* The Target Market / Audience you are trying to reach
The target audience are commercial businesses that we are selling group insurance products to
* Design Specifics; any preferences or ideas for Style, Colour, Imagery, etc
We wanted to use the Houston, Texas skyline and create something that was simple, yet modern.
* Do you have an existing website or Facebook page were designers can learn more about your company?
Yes, http://www.valmoriccorp.example and we are on Linked-In.

```html
<!DOCTYPE html>
<html lang="en">
<head>
<meta charset="utf-8">
<title>Valmoric Pocket Folder</title>
<link href="https://fonts.googleapis.com/css2?family=Exo+2:wght@500&family=Roboto:wght@400&display=swap" rel="stylesheet">
<style>
  :root {
    --stage: #dcdde0;
    --paper: #f1f2f3;
    --blue-light: #2189c7;
    --blue: #1275b8;
    --blue-deep: #0b63a6;
    --skyline: #1d5a9f;
    --ink: #58595b;
    --white: #ffffff;
  }
  * { box-sizing: border-box; }
  html, body {
    margin: 0;
    width: 1200px;
    height: 1200px;
    overflow: hidden;
    background: var(--stage);
  }
  .folder-spread {
    position: absolute;
    left: 140px;
    top: 290px;
    width: 920px;
    height: 620px;
    display: flex;
    box-shadow: 0 18px 40px rgba(0,0,0,0.18);
  }
  .panel {
    position: relative;
    width: 460px;
    height: 620px;
    overflow: hidden;
  }
  /* Back cover */
  .back-cover {
    background: linear-gradient(160deg, var(--blue-light) 0%, var(--blue) 55%, var(--blue-deep) 100%);
  }
  .back-cover .skyline {
    position: absolute;
    left: 0;
    right: 0;
    bottom: 0;
    height: 230px;
    background: linear-gradient(180deg, rgba(29,90,159,0) 0%, rgba(29,90,159,0.55) 30%, rgba(29,90,159,0.7) 100%);
  }
  .back-contact {
    position: absolute;
    left: 70px;
    top: 455px;
    width: 200px;
    text-align: center;
    color: var(--white);
    font-family: "Roboto", sans-serif;
  }
  .back-contact .company-name {
    font-family: "Exo 2", sans-serif;
    font-weight: 500;
    font-size: 30px;
    line-height: 34px;
    letter-spacing: -0.5px;
    margin: 0 0 8px;
  }
  .back-contact p {
    margin: 0;
    font-size: 8px;
    line-height: 11px;
    opacity: 0.9;
  }
  /* Front cover */
  .front-cover {
    background: var(--paper);
    border-left: 1px solid rgba(0,0,0,0.08);
  }
  .front-cover svg {
    position: absolute;
    inset: 0;
  }
  .brand {
    position: absolute;
    left: 240px;
    top: 106px;
    display: flex;
    align-items: center;
    gap: 10px;
  }
  .brand .brand-square {
    width: 30px;
    height: 30px;
    border-radius: 4px;
    background: var(--ink);
  }
  .brand .brand-name {
    font-family: "Exo 2", sans-serif;
    font-weight: 500;
    font-size: 30px;
    letter-spacing: -0.5px;
    color: var(--ink);
  }
</style>
</head>
<body>
  <main class="folder-spread">
    <section class="panel back-cover">
      <div class="skyline" role="img" aria-label="Houston skyline silhouette"></div>
      <div class="back-contact">
        <p class="company-name">Valmoric</p>
        <p>4200 Westpark Lane,</p>
        <p>Suite 310 Houston, TX 77057</p>
        <p>info@valmoriccorp.example</p>
        <p>Tel: 713-555-0142</p>
        <p>Fax: 713-555-0187</p>
        <p>Toll Free: 800-555-0119</p>
      </div>
    </section>
    <section class="panel front-cover">
      <svg width="460" height="620" viewBox="0 0 460 620">
        <defs>
          <linearGradient id="cover-blue" x1="0" y1="0" x2="0.6" y2="1">
            <stop offset="0" stop-color="#2189c7"/>
            <stop offset="0.55" stop-color="#1275b8"/>
            <stop offset="1" stop-color="#0b63a6"/>
          </linearGradient>
          <linearGradient id="skyline-tone" x1="0" y1="0" x2="0" y2="1">
            <stop offset="0" stop-color="#1d5a9f" stop-opacity="0"/>
            <stop offset="0.3" stop-color="#1d5a9f" stop-opacity="0.55"/>
            <stop offset="1" stop-color="#1d5a9f" stop-opacity="0.7"/>
          </linearGradient>
          <clipPath id="arc-clip">
            <path d="M0 0 H80 Q380 320 300 620 H0 Z"/>
          </clipPath>
        </defs>
        <path class="cover-arc" fill="url(#cover-blue)" d="M0 0 H80 Q380 320 300 620 H0 Z"/>
        <rect clip-path="url(#arc-clip)" x="0" y="390" width="460" height="230" fill="url(#skyline-tone)" role="img" aria-label="Houston skyline silhouette"/>
      </svg>
      <div class="brand">
        <span class="brand-square"></span>
        <span class="brand-name">Valmoric</span>
      </div>
    </section>
  </main>
</body>
</html>
```